Corporate Powerpoint templates

I wish to have a standardized template for our manufacturing company. We manufacture baseball caps for major sport leagues and teams.
Our powerpoint should be clean, yet stylish.
We do a lot of presentations for technical trainings, KPI reports, quality assurance training.
We have factories in China, Bangladesh, and Mexico, so the look and feel must be internationally accepted.

Target Market(s)

Branded customers

Industry/Entity Type

Headwear Manufacturing

Font styles to use
Sans Serif

Colors
00AB8E
00BBA5
67D7C9
C6EFE9
E9F9F6

Requirements
Must have
• Spreadsheet slides, graphs, photographic reports
Nice to have
• Sporty, trendy, yet corporate feel.

```html
<!DOCTYPE html>
<html lang="en">
<head>
<meta charset="utf-8">
<title>Headwear Manufacturing Presentation Template</title>
<link href="https://fonts.googleapis.com/css2?family=Poppins:wght@400;500;600;700;800&display=swap" rel="stylesheet">
<style>
:root{
  --primary:#00AB8E;
  --secondary:#00BBA5;
  --mid:#67D7C9;
  --pale:#C6EFE9;
  --mist:#E9F9F6;
  --ink:#16302c;
  --grey:#6d7a78;
  --bg:#dfe6e5;
  --white:#ffffff;
}
*{margin:0;padding:0;box-sizing:border-box}
html,body{width:1050px;height:1200px;overflow:hidden}
body{background:var(--bg);font-family:"Poppins",sans-serif;color:var(--ink);position:relative}
.slide{position:absolute;width:316px;height:178px;background:var(--white);overflow:hidden;box-shadow:0 3px 6px rgba(0,0,0,.2)}
.slide > *{position:absolute}
.col1{left:42px}.col2{left:367px}.col3{left:692px}
.row1{top:38px}.row2{top:228px}.row3{top:417px}.row4{top:606px}.row5{top:795px}.row6{top:984px}
.band{background:var(--primary)}
.display{font-family:"Poppins",sans-serif;font-weight:800;color:var(--ink);line-height:1.1;letter-spacing:-.2px}
.display.light{color:var(--white)}
.title{font-size:11.5px}
.rule{width:17px;height:5px;left:0;background:repeating-linear-gradient(var(--mid) 0 1px,transparent 1px 2px)}
.rule.light{background:repeating-linear-gradient(var(--pale) 0 1px,transparent 1px 2px)}
.url{right:8px;bottom:6px;font-size:3.6px;letter-spacing:.4px;color:var(--ink)}
.url.light{color:var(--white)}
.tiny{font-size:3.4px;line-height:1.4;color:var(--grey)}
.tiny.light{color:var(--mist)}
.label{font-size:5.6px;font-weight:600;color:var(--ink);white-space:nowrap}
.label.light{color:var(--white)}
.label.accent{color:var(--primary)}
.label.pale{color:var(--pale)}
.num{font-weight:800;color:var(--primary);font-size:11px;line-height:1}
.round{border-radius:50%}
.ring{border-radius:50%;border:5px solid var(--mid);background:var(--white)}
.dots{width:14px;height:6px;background-image:radial-gradient(var(--grey) 0.6px,transparent 0.8px);background-size:3px 3px}
.dots.light{background-image:radial-gradient(var(--pale) 0.6px,transparent 0.8px)}
.dots.accent{background-image:radial-gradient(var(--mid) 1px,transparent 1.2px)}
.icon{border-radius:50%;background:var(--primary);display:flex;align-items:center;justify-content:center}
.icon svg{width:55%;height:55%}
.boxnum{width:12px;height:12px;background:var(--primary);color:#fff;font-size:6px;font-weight:700;display:flex;align-items:center;justify-content:center}
.bullet{display:inline-block;width:4px;height:4px;border-radius:50%;background:var(--primary);margin-right:3px;vertical-align:middle}
</style>
</head>
<body>

<!-- 1 Cover -->
<section class="slide col1 row1">
  <div class="band" style="left:218px;top:0;width:98px;height:178px"></div>
  <div class="dots accent" style="left:264px;top:6px;width:40px;height:9px;background-size:12px 9px"></div>
  <div style="left:11px;top:19px;width:1px;height:67px;background:var(--ink)"></div>
  <h1 class="display" style="left:18px;top:26px;font-size:13px;line-height:1.3">Advice And<br>Counsel Throug<br>Email</h1>
  <div style="left:140px;top:34px;font-size:7px;color:var(--grey);letter-spacing:-1px">/////</div>
  <div role="img" aria-label="Portrait of a young man wearing a dark baseball cap" style="left:159px;top:21px;width:136px;height:136px;background:linear-gradient(160deg,#2e3533,#121615 55%,#5a4a3c)"></div>
  <div style="left:20px;top:107px;font-size:6.4px;font-weight:600;color:var(--primary)">We Manufacture</div>
  <div style="left:20px;top:115px;font-size:6.4px;font-weight:500;color:var(--ink);line-height:1.35">Baseball Caps For Major Sport<br>Leagues And Teams</div>
  <div style="left:20px;top:135px;width:22px;height:1px;background:var(--primary)"></div>
  <div style="left:20px;top:141px;font-size:4.6px;font-weight:600;color:var(--ink)">Go to <span style="color:var(--primary);font-weight:400">www.stitchlinecaps.com</span></div>
  <div class="ring" style="left:145px;top:143px;width:27px;height:27px"></div>
  <div class="dots light" style="left:282px;top:164px"></div>
</section>

<!-- 2 Contents -->
<section class="slide col2 row1">
  <div class="band" style="left:0;top:0;width:105px;height:178px"></div>
  <div class="rule light" style="top:18px"></div>
  <h2 class="display light title" style="left:21px;top:14px">Contents.</h2>
  <p class="tiny light" style="left:20px;top:100px;width:66px">Lorem ipsum dolor sit amet, consectetuer adipiscing elit, sed diam nonummy nibh euismod tincid</p>
  <div class="dots light" style="left:52px;top:145px"></div>
  <div class="num" style="left:133px;top:25px">1.</div>
  <div class="label" style="left:147px;top:26px">Lorem Ipsum</div>
  <p class="tiny" style="left:147px;top:34px;width:150px">Lorem ipsum dolor sit amet, consectetur adipiscing elit, sed do eiusmod tempor incididunt ut labore et dolore magna aliqua.</p>
  <div class="num" style="left:131px;top:59px">2.</div>
  <div class="label" style="left:147px;top:60px">Lorem Ipsum</div>
  <p class="tiny" style="left:147px;top:68px;width:150px">Lorem ipsum dolor sit amet, consectetuer adipiscing elit, sed diam nonummy nibh euismod tincid</p>
  <div class="num" style="left:131px;top:92px">3.</div>
  <div class="label" style="left:147px;top:93px">Lorem Ipsum</div>
  <p class="tiny" style="left:147px;top:101px;width:150px">Lorem ipsum dolor sit amet, consectetuer adipiscing elit, sed diam nonummy nibh euismod tincid</p>
  <div class="num" style="left:131px;top:127px">4.</div>
  <div class="label" style="left:147px;top:128px">Lorem Ipsum</div>
  <p class="tiny" style="left:147px;top:136px;width:150px">Lorem ipsum dolor sit amet, consectetuer adipiscing elit, sed diam nonummy nibh euismod tincid</p>
  <div class="url">www.stitchlinecaps.com</div>
</section>

<!-- 3 Agenda -->
<section class="slide col3 row1">
  <div class="band" style="left:0;top:0;width:105px;height:178px"></div>
  <div class="rule light" style="top:18px"></div>
  <h2 class="display light title" style="left:21px;top:14px">Agenda.</h2>
  <p class="tiny light" style="left:20px;top:111px;width:66px">Lorem ipsum dolor sit amet, consectetuer adipiscing elit, sed diam nonummy nibh euismod tincid</p>
  <div class="dots accent" style="left:88px;top:158px;width:30px"></div>
  <div class="dots" style="left:186px;top:18px"></div>
  <div class="dots" style="left:295px;top:122px;width:6px;height:14px"></div>
  <div class="icon" style="left:148px;top:23px;width:24px;height:24px"><svg viewBox="0 0 10 10"><rect x="2" y="1.5" width="6" height="7" fill="none" stroke="#fff" stroke-width=".9"/><path d="M3.5 4h3M3.5 6h3" stroke="#fff" stroke-width=".8"/></svg></div>
  <div class="label" style="left:130px;top:52px;width:60px;text-align:center">Lorem ipsum</div>
  <p class="tiny" style="left:125px;top:60px;width:70px;text-align:center">Lorem ipsum dolor sit amet, consectetuer adipiscing elit, sed diam nonummy nibh euismod tincidunt ut</p>
  <div class="icon" style="left:227px;top:23px;width:24px;height:24px"><svg viewBox="0 0 10 10"><path d="M2 8h6M3 7V5M5 7V3M7 7V4" stroke="#fff" stroke-width="1"/></svg></div>
  <div class="label" style="left:209px;top:52px;width:60px;text-align:center">Lorem ipsum</div>
  <p class="tiny" style="left:204px;top:60px;width:70px;text-align:center">Lorem ipsum dolor sit amet, consectetuer adipiscing elit, sed diam nonummy nibh euismod</p>
  <div class="icon" style="left:148px;top:98px;width:24px;height:24px"><svg viewBox="0 0 10 10"><rect x="1.5" y="2" width="7" height="5" rx="1" fill="#fff"/><path d="M3 7l-1 2 3-2" fill="#fff"/></svg></div>
  <div class="label" style="left:130px;top:124px;width:60px;text-align:center">Lorem ipsum</div>
  <p class="tiny" style="left:125px;top:132px;width:70px;text-align:center">unit ut dolore magna aliquam erat volutpat. Ut wisi enim ad minim veniam</p>
  <div class="icon" style="left:227px;top:98px;width:24px;height:24px"><svg viewBox="0 0 10 10"><path d="M3 2h4v2a2 2 0 0 1-4 0z" fill="#fff"/><path d="M5 6v2M3.5 8.5h3" stroke="#fff" stroke-width=".9"/></svg></div>
  <div class="label" style="left:209px;top:124px;width:60px;text-align:center">Lorem ipsum</div>
  <p class="tiny" style="left:204px;top:132px;width:70px;text-align:center">nibh euismod tincidunt ut dolore magna aliquam erat volutpat. Ut wisi enim ad minim veniam</p>
  <div class="url">www.stitchlinecaps.com</div>
</section>

<!-- 4 About Us -->
<section class="slide col1 row2">
  <div class="band" style="left:232px;top:0;width:84px;height:178px"></div>
  <div class="rule" style="top:18px"></div>
  <h2 class="display title" style="left:21px;top:14px">About Us.</h2>
  <div class="dots" style="left:162px;top:15px"></div>
  <div class="num" style="left:27px;top:50px">1.</div>
  <div class="label" style="left:40px;top:52px">Lorem Ipsum</div>
  <p class="tiny" style="left:40px;top:61px;width:135px">Lorem ipsum dolor sit amet, consectetuer adipiscing elit, sed diam nonummy nibh euismod tincidunt ut laoreet dolore.<br><br>Lorem ipsum dolor sit amet, cons ectetuer adipiscing elit, sed diam nonummy nibh euismod tincidunt ut laoreet dolor.</p>
  <div class="num" style="left:25px;top:103px">2.</div>
  <div class="label" style="left:40px;top:105px">Lorem Ipsum</div>
  <p class="tiny" style="left:40px;top:114px;width:135px">Lorem ipsum dolor sit amet, consectetuer adipiscing elit, sed diam nonummy nibh euismod tincidunt ut laoreet dolore magna aliquam erat volutpat. Ut wisi enim ad minim.</p>
  <div role="img" aria-label="Baseball player in a jersey at a stadium under lights" style="left:192px;top:28px;width:113px;height:122px;background:linear-gradient(135deg,#9cc2dc,#56768f 45%,#b54a46 72%,#6e2a28)"></div>
  <div class="ring" style="left:179px;top:139px;width:24px;height:24px"></div>
  <div class="url light">www.stitchlinecaps.com</div>
</section>

<!-- 5 Section break -->
<section class="slide col2 row2">
  <div class="band" style="left:15px;top:13px;width:286px;height:151px"></div>
  <div class="display light" style="left:15px;top:63px;width:286px;text-align:center;font-size:13.5px;letter-spacing:2px">SECTION BREAK</div>
  <div class="display" style="left:15px;top:81px;width:286px;text-align:center;font-size:13.5px;letter-spacing:2px;color:var(--pale)">SLIDE TITLE</div>
  <p class="tiny light" style="left:60px;top:103px;width:196px;text-align:center;font-size:4px">Lorem ipsum dolor sit amet, consectetuer adipiscing elit, sed diam nonummy nibh euismod tincid</p>
</section>

<!-- 6 Make Your Title -->
<section class="slide col3 row2">
  <div class="rule" style="top:18px"></div>
  <h2 class="display title" style="left:21px;top:14px">Make Your Title.</h2>
  <div class="band" style="left:0;top:66px;width:316px;height:87px"></div>
  <div class="round" style="left:45px;top:48px;width:36px;height:36px;background:#fff;border:1.5px solid var(--mid)"></div>
  <div class="round" style="left:140px;top:48px;width:36px;height:36px;background:#fff;border:1.5px solid var(--mid)"></div>
  <div class="round" style="left:235px;top:48px;width:36px;height:36px;background:#fff;border:1.5px solid var(--mid)"></div>
  <div class="num" style="left:45px;top:61px;width:36px;text-align:center;font-size:10px">01.</div>
  <div class="num" style="left:140px;top:61px;width:36px;text-align:center;font-size:10px">02.</div>
  <div class="num" style="left:235px;top:61px;width:36px;text-align:center;font-size:10px">03.</div>
  <div class="display" style="left:23px;top:90px;width:80px;text-align:center;font-size:6.4px;color:var(--pale)">Lorem ipsum</div>
  <div class="display" style="left:118px;top:90px;width:80px;text-align:center;font-size:6.4px;color:var(--pale)">Lorem ipsum</div>
  <div class="display" style="left:213px;top:90px;width:80px;text-align:center;font-size:6.4px;color:var(--pale)">Lorem ipsum</div>
  <p class="tiny light" style="left:28px;top:100px;width:70px;text-align:center;font-size:3.8px">Lorem ipsum dolor sit amet, consectetuer adipiscing elit, sed diam nonumm nibh euismod tincidunt ut laoreet dolore magna volutpat.</p>
  <p class="tiny light" style="left:123px;top:100px;width:70px;text-align:center;font-size:3.8px">Lorem ipsum dolor sit amet, consectetuer adipiscing elit, sed diam nonumm nibh euismod tincidunt ut laoreet dolore magna volutpat.</p>
  <p class="tiny light" style="left:218px;top:100px;width:70px;text-align:center;font-size:3.8px">Lorem ipsum dolor sit amet, consectetuer adipiscing elit, sed diam nonumm nibh euismod tincidunt ut laoreet dolore magna volutpat.</p>
  <div class="url">www.stitchlinecaps.com</div>
</section>

<!-- 7 Values -->
<section class="slide col1 row3">
  <div class="rule" style="top:18px"></div>
  <h2 class="display title" style="left:21px;top:14px;line-height:1.4">Lorem Ipsum<br>Dolor Sit<br>Ametkeeper.</h2>
  <div class="band" style="left:0;top:76px;width:121px;height:75px"></div>
  <p class="tiny light" style="left:21px;top:84px;width:85px;font-size:3.9px">Lorem ipsum dolor sit amet, consectetuer adipiscing elit, sed diam nonummy nibh euismod tincidunt erat volutpat.<br><br>Ut wisi enim ad minim veniam, quis nostrud exerci tation ullamcorper suscipit lobortis nisl ut aliquip ex ea commodo consequat.</p>
  <div class="icon" style="left:134px;top:28px;width:26px;height:26px"><svg viewBox="0 0 10 10"><circle cx="3.3" cy="4" r="1.1" fill="#fff"/><circle cx="6.7" cy="4" r="1.1" fill="#fff"/><circle cx="5" cy="3.3" r="1.3" fill="#fff"/><path d="M2 7.5a3 2 0 0 1 6 0z" fill="#fff"/></svg></div>
  <div class="label" style="left:170px;top:31px;font-size:6.3px">We Before Me</div>
  <p class="tiny" style="left:170px;top:40px;width:120px">ipsum dolor sit amet, cons ectetuer adipiscing elit, sed diam nonummy nibh euismod tincidunt ut laoreet</p>
  <div class="icon" style="left:134px;top:71px;width:26px;height:26px"><svg viewBox="0 0 10 10"><circle cx="3.5" cy="2.5" r="1" fill="#fff"/><circle cx="6.5" cy="2.5" r="1" fill="#fff"/><path d="M2.5 4h2v4.5h-2zM5.5 4h2v4.5h-2z" fill="#fff"/></svg></div>
  <div class="label" style="left:170px;top:73px;font-size:6.3px">We Are Good People</div>
  <p class="tiny" style="left:170px;top:82px;width:130px">ipsum dolor sit amet, cons ectetuer adipiscing elit, sed diam nonummy nibh euismod tincidunt ut laoreet dolore magna aliquam erat volutpat.</p>
  <div class="icon" style="left:134px;top:119px;width:26px;height:26px"><svg viewBox="0 0 10 10"><path d="M5 5.5 3.3 3.8a1 1 0 0 1 1.7-1 1 1 0 0 1 1.7 1z" fill="#fff"/><path d="M1.5 6.5h2l2 1h3v1H4.5l-3-.5z" fill="#fff"/></svg></div>
  <div class="label" style="left:170px;top:122px;font-size:6.3px">We Work with Heart</div>
  <p class="tiny" style="left:170px;top:131px;width:120px">ipsum dolor sit amet, cons ectetuer adipiscing elit, sed diam nonummy nibh euismod tincidunt</p>
  <div class="url">www.stitchlinecaps.com</div>
</section>

<!-- 8 Market Opportunities -->
<section class="slide col2 row3">
  <div class="rule" style="top:18px"></div>
  <h2 class="display title" style="left:23px;top:16px;font-size:10px">Market<br>Opportunities</h2>
  <p class="tiny" style="left:23px;top:47px;width:126px">Lorem ipsum dolor sit amet, consectetuer adipiscing elit, sed diam nonummy nibh euismod tincidunt ut laoreet dolore magna aliquam erat volutpat. Ut wisi enim ad minim veniam, quis nostrud exerci tation ullamcorper suscipit lobortis nisl ut aliquip ex ea commodo consequat. Duis autem vel eum iriure</p>
  <svg style="left:22px;top:84px" width="115" height="74" viewBox="0 0 115 74">
    <text x="60" y="5" font-size="4.6" font-family="Poppins,sans-serif" text-anchor="middle" fill="#16302c">Series 1</text>
    <g stroke="#dfe6e5" stroke-width=".4"><line x1="18" y1="13" x2="110" y2="13"/><line x1="18" y1="23.6" x2="110" y2="23.6"/><line x1="18" y1="34.2" x2="110" y2="34.2"/><line x1="18" y1="44.8" x2="110" y2="44.8"/><line x1="18" y1="55.4" x2="110" y2="55.4"/><line x1="18" y1="66" x2="110" y2="66"/></g>
    <g font-size="4" font-family="Poppins,sans-serif" fill="#16302c"><text x="8" y="14.5">5</text><text x="8" y="25">4</text><text x="8" y="35.5">3</text><text x="8" y="46">2</text><text x="8" y="57">1</text><text x="8" y="67.5">0</text></g>
    <rect x="24" y="23" width="10" height="43" fill="#00AB8E"/>
    <rect x="43" y="40" width="10" height="26" fill="#67D7C9"/>
    <rect x="62" y="31" width="10" height="35" fill="#00AB8E"/>
    <rect x="81" y="64" width="10" height="2" fill="#67D7C9"/>
    <g font-size="4" font-family="Poppins,sans-serif" fill="#16302c" text-anchor="middle"><text x="29" y="72">1980</text><text x="48" y="72">1990</text><text x="67" y="72">2000</text><text x="86" y="72">2010</text></g>
  </svg>
  <div class="label" style="left:193px;top:17px;font-size:7.2px">Radial Bar Chart</div>
  <svg style="left:178px;top:32px" width="100" height="100" viewBox="0 0 100 100">
    <g fill="none" transform="rotate(-90 50 50)">
      <circle cx="50" cy="50" r="44" stroke="#E9F9F6" stroke-width="8"/>
      <circle cx="50" cy="50" r="44" stroke="#00AB8E" stroke-width="8" stroke-dasharray="188 276.5"/>
      <circle cx="50" cy="50" r="34" stroke="#E9F9F6" stroke-width="8"/>
      <circle cx="50" cy="50" r="34" stroke="#67D7C9" stroke-width="8" stroke-dasharray="117 213.6"/>
      <circle cx="50" cy="50" r="24" stroke="#E9F9F6" stroke-width="8"/>
      <circle cx="50" cy="50" r="24" stroke="#00AB8E" stroke-width="8" stroke-dasharray="66 150.8"/>
      <circle cx="50" cy="50" r="15" stroke="#E9F9F6" stroke-width="8"/>
      <circle cx="50" cy="50" r="15" stroke="#67D7C9" stroke-width="8" stroke-dasharray="40 94.2"/>
    </g>
    <g font-size="3.6" font-family="Poppins,sans-serif" font-weight="600" fill="#16302c"><text x="2" y="40">68%</text><text x="17" y="80">45%</text><text x="30" y="75">35%</text><text x="40" y="68">15%</text></g>
  </svg>
  <div class="round" style="left:158px;top:140px;width:5px;height:5px;background:var(--primary)"></div>
  <div class="label" style="left:165px;top:139px;font-size:4.4px">Lorem ipsum</div>
  <p class="tiny" style="left:165px;top:145px;width:55px;font-size:2.8px">Lorem ipsum dolor sit amet, consectetuer adipiscing elit, sed diam nonummy nibh euismod tincidunt ut laoreet</p>
  <div class="round" style="left:236px;top:140px;width:5px;height:5px;background:var(--mid)"></div>
  <div class="label" style="left:243px;top:139px;font-size:4.4px">Lorem ipsum</div>
  <p class="tiny" style="left:243px;top:145px;width:55px;font-size:2.8px">Lorem ipsum dolor sit amet, consectetuer adipiscing elit, sed diam nonummy nibh euismod tincidunt ut laoreet</p>
  <div class="url">www.stitchlinecaps.com</div>
</section>

<!-- 9 Our Company -->
<section class="slide col3 row3">
  <div class="rule" style="top:18px"></div>
  <h2 class="display title" style="left:23px;top:16px">Our<br>Company</h2>
  <p class="tiny" style="left:23px;top:49px;width:95px;font-size:3.6px">Lorem ipsum dolor sit amet, consectetuer adipiscing elit, sed diam nonummy nibh euismod tincidunt ut laoreet dolore magna aliquam erat volutpat. Ut wisi enim ad minim veniam, quis nostrud exerci tation ullamcorper suscipit lobortis nisl ut aliquip ex ea commodo consequat. Duis autem vel eum iriure dolor in hendrerit i<br><br>Lorem ipsum dolor sit amet, consectetuer adipiscing elit, sed diam nonummy nibh. Lorem ipsum dolor sit amet, consectetuer adipiscing elit, sed diam nonummy nibh euismod tincidunt ut laoreet dolore magna aliquam erat volutpat. Ut wisi consectetuer adipiscing elit, sed diam nonummy nibh euismod tincidunt</p>
  <svg style="left:128px;top:28px" width="175" height="93" viewBox="0 0 175 93">
    <text x="105" y="6" font-size="5" font-family="Poppins,sans-serif" font-weight="600" text-anchor="middle" fill="#16302c">Volume</text>
    <g stroke="#dfe6e5" stroke-width=".4">
      <line x1="22" y1="12" x2="167" y2="12"/><line x1="22" y1="20.5" x2="167" y2="20.5"/><line x1="22" y1="29" x2="167" y2="29"/><line x1="22" y1="37.5" x2="167" y2="37.5"/><line x1="22" y1="46" x2="167" y2="46"/><line x1="22" y1="54.5" x2="167" y2="54.5"/><line x1="22" y1="63" x2="167" y2="63"/><line x1="22" y1="71.5" x2="167" y2="71.5"/><line x1="22" y1="80" x2="167" y2="80"/>
      <line x1="22" y1="12" x2="22" y2="80"/><line x1="167" y1="12" x2="167" y2="80"/>
    </g>
    <g font-size="4.2" font-family="Poppins,sans-serif" fill="#16302c" text-anchor="end"><text x="16" y="13.5">160</text><text x="16" y="22">140</text><text x="16" y="30.5">120</text><text x="16" y="39">100</text><text x="16" y="47.5">80</text><text x="16" y="56">60</text><text x="16" y="64.5">40</text><text x="16" y="73">20</text><text x="16" y="81.5">0</text></g>
    <rect x="32" y="50" width="14" height="30" fill="#67D7C9"/>
    <rect x="68" y="29" width="14" height="51" fill="#00AB8E"/>
    <rect x="104" y="17" width="14" height="63" fill="#67D7C9"/>
    <rect x="140" y="22" width="14" height="58" fill="#00AB8E"/>
    <g font-size="4.2" font-family="Poppins,sans-serif" fill="#16302c" text-anchor="middle"><text x="39" y="91">JAN</text><text x="75" y="91">FEB</text><text x="111" y="91">MAR</text><text x="147" y="91">APR</text></g>
  </svg>
  <div class="round" style="left:134px;top:131px;width:5px;height:5px;background:var(--mid)"></div>
  <div class="label" style="left:141px;top:130px;font-size:5px">Lorem ipsum</div>
  <p class="tiny" style="left:141px;top:136px;width:70px;font-size:2.8px">Lorem ipsum dolor sit amet, consectetuer adipiscing elit, sed diam nonummy nibh euismod tincidunt ut laoreet</p>
  <div class="round" style="left:221px;top:131px;width:5px;height:5px;background:var(--primary)"></div>
  <div class="label" style="left:228px;top:130px;font-size:5px">Lorem ipsum</div>
  <p class="tiny" style="left:228px;top:136px;width:70px;font-size:2.8px">Lorem ipsum dolor sit amet, consectetuer adipiscing elit, sed diam nonummy nibh euismod tincidunt ut laoreet</p>
  <div class="url">www.stitchlinecaps.com</div>
</section>

<!-- 10 Subject Title -->
<section class="slide col1 row4">
  <div class="rule" style="top:18px"></div>
  <h2 class="display title" style="left:21px;top:14px;line-height:1.4">Subject<br>Title.</h2>
  <div class="band" style="left:0;top:60px;width:105px;height:92px"></div>
  <p style="left:16px;top:67px;width:62px;font-size:3.5px;line-height:1.4;font-weight:600;color:#fff">Lorem ipsum dolor sit amet, consectetuer elit, sed diam nonummy nibh euismod tincidunt ut laoreet dolore magna aliquam erat volutpat. Ut wisi enim ad minim veniam, quis nostrud exerci tation ullamcorper suscipit lobortis nisl ut aliquip ex ea commodo</p>
  <div role="img" aria-label="Workers sewing caps on a factory floor" style="left:80px;top:0;width:73px;height:118px;background:linear-gradient(170deg,#8a8074,#5d6675 45%,#4d7fa6 75%,#a9bccc)"></div>
  <div role="img" aria-label="Worker in uniform operating a sewing machine" style="left:162px;top:61px;width:65px;height:106px;background:linear-gradient(160deg,#c9ccd3,#8d9199 40%,#6a5a8f 70%,#2c2c34)"></div>
  <div class="num" style="left:165px;top:21px;font-size:7.5px">1.</div>
  <div class="label" style="left:174px;top:21px">Lorem Ipsum</div>
  <p class="tiny" style="left:174px;top:29px;width:100px">Lorem ipsum dolor sit amet, consectetur adipiscing elit, sed do eiusmod tempor incididunt ut labore et dolore magna aliqua.</p>
  <div class="num" style="left:235px;top:71px;font-size:7.5px">2.</div>
  <div class="label" style="left:245px;top:71px">Lorem Ipsum</div>
  <p class="tiny" style="left:245px;top:79px;width:62px">Lorem ipsum dolor sit amet, consectetur adipiscing elit, sed do eiusmod tempor incididunt ut labore et dolore magna aliqua. tincid</p>
  <div class="num" style="left:235px;top:122px;font-size:7.5px">3.</div>
  <div class="label" style="left:245px;top:122px">Lorem Ipsum</div>
  <p class="tiny" style="left:245px;top:130px;width:62px">Lorem ipsum dolor sit amet, consectetur adipiscing elit, sed diam nonummy nibh euismod</p>
  <div class="url">www.stitchlinecaps.com</div>
</section>

<!-- 11 Text Added Here (cards) -->
<section class="slide col2 row4">
  <div class="rule" style="top:18px"></div>
  <h2 class="display title" style="left:21px;top:14px">Text Added Here</h2>
  <div class="band" style="left:27px;top:51px;width:57px;height:81px"></div>
  <div style="left:96px;top:51px;width:57px;height:81px;background:var(--mid)"></div>
  <div class="band" style="left:165px;top:51px;width:57px;height:81px"></div>
  <div style="left:234px;top:51px;width:57px;height:81px;background:var(--mid)"></div>
  <div class="icon" style="left:45px;top:40px;width:21px;height:21px;border:1.5px solid #fff;background:var(--secondary)"><svg viewBox="0 0 10 10"><rect x="2" y="2" width="6" height="6" fill="none" stroke="#fff" stroke-width=".9"/><path d="M2 4.5h6" stroke="#fff" stroke-width=".8"/></svg></div>
  <div class="icon" style="left:114px;top:40px;width:21px;height:21px;border:1.5px solid #fff;background:var(--secondary)"><svg viewBox="0 0 10 10"><rect x="2" y="2.5" width="6" height="4" fill="none" stroke="#fff" stroke-width=".9"/><path d="M5 6.5v2M3.5 8.5h3" stroke="#fff" stroke-width=".8"/></svg></div>
  <div class="icon" style="left:183px;top:40px;width:21px;height:21px;border:1.5px solid #fff;background:var(--secondary)"><svg viewBox="0 0 10 10"><path d="M1 4.5 5 2.5l4 2-4 2z" fill="#fff"/><path d="M3 5.5v1.5c1 1 3 1 4 0V5.5" fill="#fff"/></svg></div>
  <div class="icon" style="left:252px;top:40px;width:21px;height:21px;border:1.5px solid #fff;background:var(--secondary)"><svg viewBox="0 0 10 10"><rect x="2" y="2.5" width="6" height="5" rx=".6" fill="#fff"/></svg></div>
  <div class="label light" style="left:34px;top:67px;font-size:5.4px">Lorem ipsum</div>
  <p class="tiny light" style="left:34px;top:74px;width:45px;font-size:3px">ipsum dolor sit amet, cons ectetuer adipiscing elit, sed diam nonummy nibh euismod tincidunt ut laoreet<br><br>ipsum dolor sit amet, cons ectetuer adipiscing elit, sed diam nonummy nibh euismod tincidunt ut laoreet</p>
  <div class="label" style="left:103px;top:67px;font-size:5.4px">Lorem ipsum</div>
  <p class="tiny" style="left:103px;top:74px;width:45px;font-size:3px;color:var(--ink)">ipsum dolor sit amet, cons ectetuer adipiscing elit, sed diam nonummy nibh euismod tincidunt ut laoreet<br><br>ipsum dolor sit amet, cons ectetuer adipiscing elit, sed diam nonummy nibh euismod tincidunt ut laoreet</p>
  <div class="label light" style="left:172px;top:67px;font-size:5.4px">Lorem ipsum</div>
  <p class="tiny light" style="left:172px;top:74px;width:45px;font-size:3px">ipsum dolor sit amet, cons ectetuer adipiscing elit, sed diam nonummy nibh euismod tincidunt ut laoreet<br><br>ipsum dolor sit amet, cons ectetuer adipiscing elit, sed diam nonummy nibh euismod tincidunt ut laoreet</p>
  <div class="label" style="left:241px;top:67px;font-size:5.4px">Lorem ipsum</div>
  <p class="tiny" style="left:241px;top:74px;width:45px;font-size:3px;color:var(--ink)">ipsum dolor sit amet, cons ectetuer adipiscing elit, sed diam nonummy nibh euismod tincidunt ut laoreet<br><br>ipsum dolor sit amet, cons ectetuer adipiscing elit, sed diam nonummy nibh euismod tincidunt ut laoreet</p>
  <div style="left:27px;top:139px;font-size:11px;font-weight:600;color:var(--primary)">+ 35k</div>
  <p class="tiny" style="left:27px;top:156px;width:210px;font-size:3px">Lorem ipsum dolor sit amet, consectetuer adipiscing elit, sed diam nonummy nibh euismod tincidunt ut laoreet dolore magna aliquam erat volutpat. Ut wisi enim ad minim veniam, quis nostrud exerci tation ullamcorper</p>
  <div class="url">www.stitchlinecaps.com</div>
</section>

<!-- 12 Text Added Here (circles) -->
<section class="slide col3 row4">
  <div class="band" style="left:0;top:0;width:316px;height:82px"></div>
  <div class="rule light" style="top:18px"></div>
  <h2 class="display light title" style="left:21px;top:14px">Text Added Here</h2>
  <div class="round" role="img" aria-label="Cap being pressed on a heat press machine" style="left:27px;top:47px;width:70px;height:70px;border:3px solid #fff;background:radial-gradient(circle at 50% 40%,#4a6fa8,#22304e 55%,#3b2a20)"></div>
  <div class="round" role="img" aria-label="Baseball players in jerseys celebrating" style="left:118px;top:47px;width:70px;height:70px;border:3px solid #fff;background:radial-gradient(circle at 50% 40%,#d8b85a,#7b8a4a 50%,#1d4d2c)"></div>
  <div class="round" role="img" aria-label="Rows of colorful numbered caps on display" style="left:212px;top:47px;width:70px;height:70px;border:3px solid #fff;background:radial-gradient(circle at 50% 45%,#c34a3a,#2f7a46 45%,#1b1b22)"></div>
  <div class="label" style="left:24px;top:125px">Laoreet Dolore</div>
  <p class="tiny" style="left:24px;top:133px;width:80px">Lorem ipsum dolor sit amet, consectetuer adipiscing elit, sed diam nonummy nibh euismod tincidunt ut</p>
  <div class="label" style="left:115px;top:125px">Laoreet Dolore</div>
  <p class="tiny" style="left:115px;top:133px;width:80px">Lorem ipsum dolor sit amet, consectetuer adipiscing elit, sed diam nonummy nibh euismod tincidunt ut</p>
  <div class="label" style="left:209px;top:125px">Laoreet Dolore</div>
  <p class="tiny" style="left:209px;top:133px;width:80px">Lorem ipsum dolor sit amet, consectetuer adipiscing elit, sed diam nonummy nibh euismod tincidunt ut</p>
  <div class="url">www.stitchlinecaps.com</div>
</section>

<!-- 13 Summary -->
<section class="slide col1 row5">
  <div class="band" style="left:0;top:0;width:107px;height:178px"></div>
  <div class="rule light" style="top:18px"></div>
  <h2 class="display light title" style="left:21px;top:14px">Summary</h2>
  <p class="tiny light" style="left:21px;top:36px;width:72px;font-size:3.8px">Lorem ipsum dolor sit amet, consectetuer adipiscing elit, sed diam nonummy nibh .<br><br>Ut wisi enim ad minim veniam, quis nostrud exerci tation ullamcorper suscipit lobortis.</p>
  <div class="round" style="left:29px;top:90px;width:4px;height:4px;background:var(--pale)"></div>
  <div class="label pale" style="left:37px;top:88px;font-size:4.4px">Lorem ipsum</div>
  <p class="tiny light" style="left:37px;top:94px;width:45px;font-size:2.8px">Lorem ipsum dolor sit amet, consectetuer adipiscing elit, sed diam nonummy</p>
  <div class="round" style="left:29px;top:112px;width:4px;height:4px;background:var(--pale)"></div>
  <div class="label pale" style="left:37px;top:110px;font-size:4.4px">Lorem ipsum</div>
  <p class="tiny light" style="left:37px;top:116px;width:45px;font-size:2.8px">Lorem ipsum dolor sit amet, consectetuer adipiscing elit, sed diam nonummy</p>
  <div class="round" style="left:29px;top:135px;width:4px;height:4px;background:var(--pale)"></div>
  <div class="label pale" style="left:37px;top:133px;font-size:4.4px">Lorem ipsum</div>
  <p class="tiny light" style="left:37px;top:139px;width:45px;font-size:2.8px">Lorem ipsum dolor sit amet, consectetuer adipiscing elit, sed diam nonummy</p>
  <div class="dots light" style="left:80px;top:160px"></div>
  <div class="dots" style="left:120px;top:16px"></div>
  <svg style="left:107px;top:0" width="209" height="178" viewBox="0 0 209 178">
    <path d="M35 100 V78 A50 50 0 0 1 118 40" fill="none" stroke="#16302c" stroke-width="2"/>
    <path d="M29 92 35 102 41 92" fill="none" stroke="#16302c" stroke-width="2"/>
    <path d="M148 56 Q165 82 143 98 Q132 120 118 128 Q88 146 58 128" fill="none" stroke="#16302c" stroke-width="2"/>
    <path d="M40 112 L52 122" stroke="#16302c" stroke-width="1"/>
    <circle cx="40" cy="112" r="2.5" fill="#16302c"/>
    <circle cx="133" cy="48" r="17" fill="#fff" stroke="#16302c" stroke-width="2.5"/>
    <circle cx="133" cy="48" r="12" fill="#00AB8E"/>
    <circle cx="133" cy="48" r="5" fill="#fff"/>
    <circle cx="143" cy="98" r="12" fill="#fff" stroke="#16302c" stroke-width="2.5"/>
    <circle cx="143" cy="98" r="6" fill="none" stroke="#00AB8E" stroke-width="2"/>
    <circle cx="118" cy="128" r="9" fill="#fff" stroke="#16302c" stroke-width="2.5"/>
    <circle cx="118" cy="128" r="3.5" fill="#00AB8E"/>
    <circle cx="58" cy="128" r="8" fill="#fff" stroke="#16302c" stroke-width="2.5"/>
    <circle cx="58" cy="128" r="3" fill="#00AB8E"/>
    <g fill="#00AB8E"><rect x="67" y="62" width="2" height="8"/><rect x="70" y="65" width="2" height="5"/><rect x="73" y="60" width="2" height="10"/><rect x="76" y="64" width="2" height="6"/></g>
    <text x="72" y="77" font-size="5" font-weight="600" font-family="Poppins,sans-serif" text-anchor="middle" fill="#16302c">MAIN TITLE</text>
    <text x="72" y="82" font-size="2.5" font-family="Poppins,sans-serif" text-anchor="middle" fill="#6d7a78">Lorem ipsum dolor sit amet,</text>
    <text x="72" y="85" font-size="2.5" font-family="Poppins,sans-serif" text-anchor="middle" fill="#6d7a78">consectetuer adipiscing</text>
    <g font-size="3.4" font-family="Poppins,sans-serif" font-style="italic" font-weight="600" fill="#00AB8E">
      <path d="M148 38 157 34" stroke="#00AB8E" stroke-width=".6"/><text x="159" y="35">85%</text>
      <path d="M120 90 129 92" stroke="#00AB8E" stroke-width=".6"/><text x="109" y="91">80%</text>
      <path d="M67 126 77 121" stroke="#00AB8E" stroke-width=".6"/><text x="79" y="122">50%</text>
      <path d="M126 134 134 140" stroke="#00AB8E" stroke-width=".6"/><text x="136" y="143">75%</text>
    </g>
    <g font-size="4.2" font-weight="600" font-family="Poppins,sans-serif" fill="#16302c"><text x="168" y="47">Your Title</text><text x="168" y="93">Your Title</text><text x="8" y="126">Your Title</text><text x="156" y="132">Your Title</text></g>
    <g font-size="2.4" font-family="Poppins,sans-serif" fill="#6d7a78"><text x="168" y="52">Lorem ipsum dolor sit</text><text x="168" y="55">consectetuer adipiscing</text><text x="168" y="98">Lorem ipsum dolor sit</text><text x="168" y="101">consectetuer adipiscing</text><text x="6" y="131">Lorem ipsum dolor sit</text><text x="6" y="134">consectetuer adipisc</text><text x="156" y="137">Lorem ipsum dolor sit</text><text x="156" y="140">consectetuer adipisc</text></g>
  </svg>
  <div class="url">www.stitchlinecaps.com</div>
</section>

<!-- 14 Timeline -->
<section class="slide col2 row5">
  <div class="rule" style="top:18px"></div>
  <h2 class="display title" style="left:21px;top:14px">Our Timeline</h2>
  <div class="dots" style="left:295px;top:16px;width:6px;height:30px"></div>
  <svg style="left:10px;top:34px" width="290" height="102" viewBox="0 0 290 102">
    <line x1="50" y1="3" x2="50" y2="86" stroke="#16302c" stroke-width=".6"/>
    <circle cx="50" cy="3" r="1.2" fill="#16302c"/>
    <line x1="50" y1="86" x2="260" y2="86" stroke="#16302c" stroke-width=".6"/>
    <g fill="#16302c"><circle cx="50" cy="86" r="1.3"/><circle cx="71" cy="86" r="1.3"/><circle cx="92" cy="86" r="1.3"/><circle cx="113" cy="86" r="1.3"/><circle cx="134" cy="86" r="1.3"/><circle cx="155" cy="86" r="1.3"/><circle cx="176" cy="86" r="1.3"/><circle cx="197" cy="86" r="1.3"/><circle cx="218" cy="86" r="1.3"/><circle cx="239" cy="86" r="1.3"/><circle cx="260" cy="86" r="1.3"/></g>
    <g font-size="4.4" font-family="Poppins,sans-serif" fill="#16302c" text-anchor="middle"><text x="50" y="96">0%</text><text x="71" y="96">10%</text><text x="92" y="96">20%</text><text x="113" y="96">30%</text><text x="134" y="96">40%</text><text x="155" y="96">50%</text><text x="176" y="96">60%</text><text x="197" y="96">70%</text><text x="218" y="96">80%</text><text x="239" y="96">90%</text><text x="260" y="96">100%</text></g>
    <g fill="#00AB8E"><circle cx="16" cy="24" r="2.5"/><circle cx="16" cy="48" r="2.5"/><circle cx="16" cy="72" r="2.5"/></g>
    <g font-size="5.2" font-weight="600" font-family="Poppins,sans-serif" fill="#16302c"><text x="22" y="26">2019</text><text x="22" y="50">2020</text><text x="22" y="74">2021</text></g>
    <rect x="50" y="15" width="26" height="17" fill="#00AB8E"/><rect x="76" y="15" width="53" height="17" fill="#67D7C9"/><rect x="129" y="15" width="13" height="17" fill="#00AB8E"/><rect x="142" y="15" width="118" height="17" fill="#67D7C9"/>
    <rect x="50" y="39" width="88" height="17" fill="#00AB8E"/><rect x="138" y="39" width="52" height="17" fill="#67D7C9"/><rect x="190" y="39" width="35" height="17" fill="#00AB8E"/><rect x="225" y="39" width="35" height="17" fill="#67D7C9"/>
    <rect x="50" y="63" width="37" height="17" fill="#67D7C9"/><rect x="87" y="63" width="74" height="17" fill="#00AB8E"/><rect x="161" y="63" width="13" height="17" fill="#67D7C9"/><rect x="174" y="63" width="86" height="17" fill="#00AB8E"/>
    <g font-size="4.4" font-family="Poppins,sans-serif" text-anchor="middle">
      <text x="63" y="25" fill="#fff">20%</text><text x="102.5" y="25" fill="#16302c">40%</text><text x="135.5" y="25" fill="#fff">10%</text><text x="201" y="25" fill="#16302c">90%</text>
      <text x="94" y="49" fill="#fff">50%</text><text x="164" y="49" fill="#16302c">30%</text><text x="207.5" y="49" fill="#fff">20%</text><text x="242.5" y="49" fill="#16302c">20%</text>
      <text x="68.5" y="73" fill="#16302c">30%</text><text x="124" y="73" fill="#fff">60%</text><text x="167.5" y="73" fill="#16302c">10%</text><text x="217" y="73" fill="#fff">70%</text>
    </g>
  </svg>
  <div class="label" style="left:57px;top:138px;font-size:4.2px">LOREM IPSUM</div>
  <p class="tiny" style="left:57px;top:143px;width:46px;font-size:2.6px">Lorem ipsum dolor sit amet, consectetuer adipiscing elit, sed diam nonummy nibh euismod tincid</p>
  <div class="label accent" style="left:112px;top:138px;font-size:4.2px">LOREM IPSUM</div>
  <p class="tiny" style="left:112px;top:143px;width:46px;font-size:2.6px">Lorem ipsum dolor sit amet, consectetuer adipiscing elit, sed diam nonummy nibh euismod tincid</p>
  <div class="label" style="left:170px;top:138px;font-size:4.2px">LOREM IPSUM</div>
  <p class="tiny" style="left:170px;top:143px;width:46px;font-size:2.6px">Lorem ipsum dolor sit amet, consectetuer adipiscing elit, sed diam nonummy nibh euismod tincid</p>
  <div class="label accent" style="left:229px;top:138px;font-size:4.2px">LOREM IPSUM</div>
  <p class="tiny" style="left:229px;top:143px;width:46px;font-size:2.6px">Lorem ipsum dolor sit amet, consectetuer adipiscing elit, sed diam nonummy nibh euismod tincid</p>
  <div class="dots" style="left:14px;top:158px"></div>
  <div class="url">www.stitchlinecaps.com</div>
</section>

<!-- 15 Two columns -->
<section class="slide col3 row5">
  <div class="rule" style="top:18px"></div>
  <h2 class="display title" style="left:21px;top:16px">Text Added Here</h2>
  <div class="label" style="left:32px;top:37px;font-size:6.4px;font-weight:500">1. Text Added Here</div>
  <p class="tiny" style="left:32px;top:47px;width:115px;font-size:3px">Lorem ipsum dolor sit amet, consectetuer adipiscing elit, sed diam nonummy nibh euismod tincidunt ut laoreet dolore magna aliquam erat volutpat. Ut wisi enim ad minim veniam, quis nostrud exerci tation ullamcorper suscipit lobortis nisl ut aliquip ex ea commodo consequat.<br><br>Lorem ipsum dolor sit amet, consectetuer adipiscing elit, sed diam nonummy nibh euismod tincidunt ut laoreet dolore magna aliquam erat volutpat. Ut wisi enim ad minim veniam, quis nostrud exerci tation ullamcorper suscipit lobortis nisl ut aliquip ex ea commodo consequat.</p>
  <div class="label" style="left:163px;top:37px;font-size:6.4px;font-weight:500">2. Text Added Here</div>
  <p class="tiny" style="left:163px;top:47px;width:115px;font-size:3px">Lorem ipsum dolor sit amet, consectetuer adipiscing elit, sed diam nonummy nibh euismod tincidunt ut laoreet dolore magna aliquam erat volutpat. Ut wisi enim ad minim veniam, quis nostrud exerci tation ullamcorper suscipit lobortis nisl ut aliquip ex ea commodo consequat.<br><br>Lorem ipsum dolor sit amet, consectetuer adipiscing elit, sed diam nonummy nibh euismod tincidunt ut laoreet dolore magna aliquam erat volutpat. Ut wisi enim ad minim veniam, quis nostrud exerci tation ullamcorper suscipit lobortis nisl ut aliquip ex ea commodo consequat.</p>
  <div class="boxnum" style="left:40px;top:107px">1.</div>
  <div class="label" style="left:56px;top:106px">Lorem ipsum</div>
  <p class="tiny" style="left:56px;top:113px;width:80px;font-size:3px">Lorem ipsum dolor sit amet, consectetuer adipiscing elit, sed diam nonummy nibh</p>
  <div class="boxnum" style="left:40px;top:135px">2.</div>
  <div class="label" style="left:56px;top:134px">Lorem ipsum</div>
  <p class="tiny" style="left:56px;top:141px;width:80px;font-size:3px">Lorem ipsum dolor sit amet, consectetuer adipiscing elit, sed diam nonummy nibh</p>
  <div class="boxnum" style="left:175px;top:105px">1.</div>
  <div class="label" style="left:191px;top:104px">Lorem ipsum</div>
  <p class="tiny" style="left:191px;top:111px;width:80px;font-size:3px">Lorem ipsum dolor sit amet, consectetuer adipiscing elit, sed diam nonummy nibh</p>
  <div class="boxnum" style="left:175px;top:133px">2.</div>
  <div class="label" style="left:191px;top:132px">Lorem ipsum</div>
  <p class="tiny" style="left:191px;top:139px;width:80px;font-size:3px">Lorem ipsum dolor sit amet, consectetuer adipiscing elit, sed diam nonummy nibh</p>
  <div class="url">www.stitchlinecaps.com</div>
</section>

<!-- 16 Our Member -->
<section class="slide col1 row6">
  <div class="rule" style="top:18px"></div>
  <h2 class="display title" style="left:21px;top:14px">Our Member</h2>
  <div class="dots" style="left:265px;top:34px"></div>
  <div class="band" style="left:30px;top:75px;width:48px;height:84px"></div>
  <div class="round" role="img" aria-label="Member photo placeholder" style="left:31px;top:52px;width:46px;height:46px;background:var(--pale);border:2px solid #fff"></div>
  <div style="left:37px;top:103px;font-size:4.8px;font-weight:600;color:#fff;line-height:1.35">Lorem<br>Ipsum<br><span style="color:var(--pale)">Dolor Sit<br>Amet,<br>Consec-<br>teteur</span><br>Adipiscing</div>
  <div style="left:85px;top:55px;font-size:8.6px;font-weight:700;color:var(--ink)">YOUR NAME</div>
  <div style="left:85px;top:66px;font-size:6.2px;color:var(--grey)">Position</div>
  <div style="left:113px;top:70px;width:24px;height:1px;background:var(--primary)"></div>
  <p class="tiny" style="left:85px;top:83px;width:202px;font-size:3.5px;line-height:1.3">Lorem ipsum dolor sit amet, consectetuer adipiscing elit, sed diam nonummy nibh euismod tincidunt ut laoreet dolore magna aliquam erat volutpat. Ut wisi enim ad minim veniam, quis nostrud exerci tation ullamcorper suscipit lobortis nisl ut aliquip ex ea commodo consequat. Duis autem vel eum iriure dolor in hendrerit in vulputate velit esse molestie consequat, vel illum dolore eu feugiat nulla facilisis at vero eros et accumsan et iusto odio dignissim qui blandit praesent luptatum zzril delenit augue duis dolore te feugait nulla facilisi.<br><br>Lorem ipsum dolor sit amet, cons ectetuer adipiscing elit, sed diam nonummy nibh euismod tincidunt ut laoreet dolore magna aliquam erat volutpat. Ut wisi enim ad minim veniam, quis nostrud exerci tation ullamcorper suscipit lobortis nisl ut aliquip ex ea commodo consequat. Lorem ipsum dolor sit amet, consectetuer adipiscing elit, sed diam nonummy nibh euismod tincidunt ut laoreet dolore magna aliquam erat volutpat.</p>
  <div class="dots" style="left:66px;top:166px"></div>
  <div class="url">www.stitchlinecaps.com</div>
</section>

<!-- 17 Team Members -->
<section class="slide col2 row6">
  <div class="rule" style="top:18px"></div>
  <h2 class="display title" style="left:21px;top:14px">Team Members.</h2>
  <p class="tiny" style="left:21px;top:31px;width:250px;font-size:3.7px">Lorem ipsum dolor sit amet, consectetuer adipiscing elit, sed diam nonummy nibh euismod tincim veniam, quis nostrud exerci tation ullamcorper suscipit lobortis nisl ut aliquip ex ea commodo consequat. Duis autem</p>
  <div class="band" style="left:0;top:84px;width:316px;height:94px"></div>
  <div class="round" role="img" aria-label="Team member headshot" style="left:38px;top:60px;width:49px;height:49px;background:var(--mist);border:2px solid #fff"></div>
  <div class="round" role="img" aria-label="Team member headshot" style="left:134px;top:60px;width:49px;height:49px;background:var(--mist);border:2px solid #fff"></div>
  <div class="round" role="img" aria-label="Team member headshot" style="left:230px;top:60px;width:49px;height:49px;background:var(--mist);border:2px solid #fff"></div>
  <div style="left:22px;top:116px;width:80px;text-align:center;font-size:6.6px;font-weight:600;color:var(--pale)">DANIEL REYES</div>
  <div style="left:118px;top:116px;width:80px;text-align:center;font-size:6.6px;font-weight:600;color:var(--pale)">AMARA OKAFOR</div>
  <div style="left:214px;top:116px;width:80px;text-align:center;font-size:6.6px;font-weight:600;color:var(--pale)">LUCAS BRANDT</div>
  <p class="tiny light" style="left:32px;top:126px;width:60px;text-align:center;font-size:3px">ipsum dolor sit amet, cons ectetuer adipiscing elit, sed diam nonummy nibh euismod tincidunt ut laoreet dolore magna aliquam erat volutpat. Ut wisi enim ad minim veniam, quis nostrud</p>
  <p class="tiny light" style="left:128px;top:126px;width:60px;text-align:center;font-size:3px">ipsum dolor sit amet, cons ectetuer adipiscing elit, sed diam nonummy nibh euismod tincidunt ut laoreet dolore magna aliquam erat volutpat. Ut wisi enim ad minim veniam, quis nostrud</p>
  <p class="tiny light" style="left:224px;top:126px;width:60px;text-align:center;font-size:3px">ipsum dolor sit amet, cons ectetuer adipiscing elit, sed diam nonummy nibh euismod tincidunt ut laoreet dolore magna aliquam erat volutpat. Ut wisi enim ad minim veniam, quis nostrud</p>
  <div class="url light">www.stitchlinecaps.com</div>
</section>

<!-- 18 Thank You -->
<section class="slide col3 row6">
  <div class="band" style="left:217px;top:0;width:99px;height:178px"></div>
  <div class="dots accent" style="left:264px;top:6px;width:40px;height:9px;background-size:12px 9px"></div>
  <div style="left:13px;top:17px;width:1px;height:92px;background:var(--ink)"></div>
  <h2 class="display" style="left:21px;top:22px;font-size:25px;line-height:1.1">Thank<br>You</h2>
  <div style="left:143px;top:38px;font-size:7px;color:var(--grey);letter-spacing:-1px">///</div>
  <div role="img" aria-label="Dark trucker cap with embroidered patch on a display" style="left:159px;top:22px;width:136px;height:135px;background:linear-gradient(150deg,#8a8680,#2d2d30 45%,#1a1a1c 70%,#6b6a5a)"></div>
  <div class="display" style="left:21px;top:105px;font-size:8px">Contact US</div>
  <div style="left:21px;top:116px;width:23px;height:1px;background:var(--primary)"></div>
  <div style="left:21px;top:120px;font-size:5.2px;color:var(--ink);line-height:1.55;white-space:nowrap">
    <div><span class="bullet"></span>555-010-2048</div>
    <div><span class="bullet"></span>hello@stitchlinecaps.com</div>
    <div><span class="bullet"></span>18 Loom Street, Riverton, box 40210</div>
  </div>
  <div class="ring" style="left:145px;top:143px;width:27px;height:27px"></div>
  <div class="dots light" style="left:280px;top:164px"></div>
</section>

</body>
</html>
```